Meridale Vantage Alliance Web Design

I would like a web design for a conference. Registration, Form completion, Hotel, Speakers etc. See link for sample similar but not the same.
http://qrvlo.example/pldwk/index.php/contact-us
We would like the design to depict the colours of the logo which is attached. A banner of the website will be provided. We would like a transitioning space in the top and front page of the website for announcements and showcase of events. We would like custom prepared headers for each grouping, example, Sponsor, Venue, Discussion etc.

Hotel

Coded - Design and coding required

```html
<!DOCTYPE html>
<html lang="en">
<head>
<meta charset="utf-8">
<title>Meridale Vantage Alliance Conference 2015</title>
<link href="https://fonts.googleapis.com/css2?family=Open+Sans:ital,wght@0,300;0,400;0,600;0,700;1,400&display=swap" rel="stylesheet">
<style>
:root{
  --navy:#1a3a66;
  --footer:#0d3a5c;
  --footer-dark:#0a2238;
  --blue:#1c86d6;
  --red:#e8202a;
  --yellow:#f5b800;
  --orange:#f08a1e;
  --teal:#12ac9e;
  --teal-dark:#0e7f7a;
  --green:#6ab82e;
  --black:#141414;
  --text:#444;
  --muted:#777;
  --grey-band:#e3e3e3;
}
*{margin:0;padding:0;box-sizing:border-box}
html,body{width:1200px;height:2235px;overflow:hidden;background:#fff}
body{font-family:"Open Sans",Arial,sans-serif;color:var(--text);position:relative}
.strip{position:absolute;left:0;width:1200px;height:6px;display:flex}
.strip span{flex:1}
/* header */
.site-header{position:absolute;top:6px;left:0;width:1200px;height:97px;background:#fff}
.brand{position:absolute;left:94px;top:14px;display:flex;align-items:center;gap:12px}
.brand-mark{width:62px;height:62px;border-radius:50%;border:6px solid var(--blue)}
.brand-name{font-size:18px;font-weight:700;color:var(--red);line-height:1.1;width:250px;text-transform:uppercase}
.social{position:absolute;right:98px;top:16px;display:flex;gap:10px}
.social span{width:20px;height:20px;border-radius:50%;background:#222}
.main-nav{position:absolute;left:391px;top:66px;width:711px;display:flex;justify-content:space-between;font-size:11px;font-weight:600;color:#222;text-transform:uppercase}
/* hero */
.hero{position:absolute;top:103px;left:0;width:1200px;height:597px;background:linear-gradient(180deg,#6b6a5a 0%,#4a4a42 45%,#3b3933 100%)}
.info-card{position:absolute;top:380px;height:272px;width:320px;color:#fff;text-align:center;padding:20px 26px}
.info-card h2{font-size:24px;font-weight:600;margin:14px 0 16px;text-transform:uppercase}
.info-card p{font-size:14.5px;line-height:1.45}
.card-venue{left:94px;background:var(--blue)}
.card-welcome{left:447px;background:var(--red)}
.card-news{left:789px;width:317px;background:var(--yellow);text-align:left;padding:20px 22px}
.card-news h2{margin:0 0 12px 0;display:flex;align-items:center;gap:12px;color:#222}
.card-news .date{font-style:italic;font-weight:700;font-size:14px;color:#222;margin-top:8px}
.card-news p{color:#222;font-size:14px}
/* thanks */
.thanks{position:absolute;left:94px;top:735px}
.thanks h1{font-size:38px;font-weight:300;color:var(--red)}
.thanks p{font-size:20px;font-weight:300;color:var(--muted);margin-top:6px}
.thanks p b{color:var(--red);font-weight:400}
.register{position:absolute;left:787px;top:700px;width:319px;height:134px;background:var(--teal);color:#fff;padding:38px 20px}
.register::before{content:"";position:absolute;left:0;top:0;width:100%;height:22px;background:var(--teal-dark)}
.register .small{font-size:20px;font-weight:600}
.register .big{font-size:25px;font-weight:600}
.register .go{position:absolute;right:18px;top:52px;width:54px;height:54px}
/* tabs */
.tab{position:absolute;left:94px;width:319px;height:116px;color:#fff;display:flex;align-items:center;padding-left:18px}
.tab::before{content:"";position:absolute;left:20px;top:18px;width:20px;height:3px;background:#fff}
.tab::after{content:"";position:absolute;right:-14px;top:44px;border-left:14px solid var(--c);border-top:14px solid transparent;border-bottom:14px solid transparent}
.tab .num{font-size:52px;font-weight:300;width:100px}
.tab .lbl{font-size:24px;font-weight:400;line-height:1.2}
.tab-1{top:872px;background:var(--navy);--c:var(--navy)}
.tab-2{top:988px;background:var(--blue);--c:var(--blue)}
.tab-3{top:1104px;background:var(--teal);--c:var(--teal)}
.tab-text{position:absolute;left:442px;width:318px;font-size:12.5px;line-height:1.5;color:#555}
.tab-text::before{content:"";display:block;width:22px;height:3px;background:#222;margin-bottom:8px}
.tab-text .more{display:block;font-size:11px;font-weight:700;color:#333;margin-top:4px}
.feature{position:absolute;left:787px;width:319px}
.feature .caption{position:absolute;left:0;bottom:0;width:100%;height:40px;background:rgba(0,0,0,.6);color:#fff;font-size:16px;padding:9px 14px}
/* speakers */
.section-title{position:absolute;left:94px;top:1250px;font-size:36px;font-weight:400;color:#222}
.speaker{position:absolute;width:322px;height:140px;display:flex;color:#fff}
.speaker .photo{width:157px;height:100%}
.speaker .bio{flex:1;padding:12px 12px}
.speaker h3{font-size:12px;font-weight:600;text-transform:uppercase;line-height:1.25}
.speaker p{font-size:11.5px;font-style:italic;line-height:1.3;margin-top:8px}
/* sponsors */
.sponsors{position:absolute;top:1658px;left:0;width:1200px;height:130px;background:var(--grey-band);display:flex;align-items:center;justify-content:space-between;padding:0 110px}
.sponsor{font-size:26px;font-weight:600;color:#666}
/* footer */
.site-footer{position:absolute;top:1788px;left:0;width:1200px;height:362px;background:var(--footer);color:#fff}
.col{position:absolute;top:62px}
.col h4{font-size:16px;font-weight:400;text-transform:uppercase;letter-spacing:.3px;margin-bottom:22px}
.col ul{list-style:none;font-size:13px;width:180px}
.col li{padding:5px 0;border-bottom:1px solid rgba(255,255,255,.35)}
.field{width:246px;height:32px;background:#c9d3dc;color:#333;font-size:13px;padding:7px 12px;margin-bottom:8px}
.field.tall{height:72px}
.submit{width:86px;height:30px;background:var(--orange);color:#fff;font-size:13px;text-align:center;line-height:30px}
.copyright{position:absolute;top:2150px;left:0;width:1200px;height:79px;background:var(--footer-dark);color:#4aa3e0;font-size:14px;padding:32px 94px}
</style>
</head>
<body>
<div class="strip" style="top:0"><span style="background:var(--blue)"></span><span style="background:var(--red)"></span><span style="background:var(--yellow)"></span><span style="background:var(--teal)"></span><span style="background:var(--green)"></span><span style="background:var(--orange)"></span></div>

<header class="site-header">
  <div class="brand"><span class="brand-mark"></span><span class="brand-name">Meridale Vantage Alliance Conference 2015</span></div>
  <div class="social"><span></span><span></span><span></span></div>
  <nav class="main-nav"><span>Home</span><span>Conference</span><span>Programme</span><span>Speakers</span><span>Presentation</span><span>Hotel</span><span>Gallery</span><span>Contact Us</span></nav>
</header>

<div class="hero" role="img" aria-label="Group photograph of conference delegates standing on a lawn"></div>

<section class="info-card card-venue">
  <svg width="30" height="30" viewBox="0 0 30 30"><circle cx="15" cy="10" r="6" fill="none" stroke="#fff" stroke-width="2.5"/><path d="M15 16v6M4 26h22M8 26l3-6M22 26l-3-6" stroke="#fff" stroke-width="2.5" fill="none"/></svg>
  <h2>Venue</h2>
  <p>Conference and Accomodation<br>Larkspur Bay Resort &amp; Spa<br>Jamaica, West Indies</p>
  <p style="margin-top:14px"><b>Phone:</b> 1-(555) -010-2200,<br><b>Fax:</b> 1-(555)-010-2205<br><b>Email:</b> info@mvac.example</p>
</section>
<section class="info-card card-welcome">
  <svg width="30" height="30" viewBox="0 0 30 30"><rect x="5" y="3" width="20" height="24" rx="2" fill="none" stroke="#fff" stroke-width="2.5"/><path d="M10 11h10M10 16h10M10 21h6" stroke="#fff" stroke-width="2.5"/></svg>
  <h2>9th MVAC</h2>
  <p>I gives me great pleasure to welcome you all to the 8th Meridale Conference on Healthcare Financing.</p>
  <p style="margin-top:18px">Members of the Secretariat (Meridale Health Fund Staff) and</p>
</section>
<section class="info-card card-news">
  <h2><svg width="30" height="26" viewBox="0 0 30 26"><path d="M2 9h6l14-7v22L8 17H2z" fill="#222"/><path d="M6 17l3 8h4l-3-8" fill="#222"/></svg>Announcements</h2>
  <div class="date">20th may 2015</div>
  <p>Members of the Secretariat (Meridale Health Fund Staff) and Board of Directors and will be onsite.</p>
  <div class="date" style="margin-top:14px">20th may 2015</div>
  <p>Members of the Secretariat (Meridale Health Fund Staff) and Board of Directors and will be onsite.</p>
</section>

<section class="thanks">
  <h1>A Big Thank You!! to all participants</h1>
  <p>and sponsors for making the <b>8th hosting</b> of this conference a success.</p>
</section>
<a class="register">
  <div class="small">Conference</div>
  <div class="big">REGISTRATION</div>
  <svg class="go" viewBox="0 0 56 56"><circle cx="28" cy="28" r="28" fill="#fff"/><path d="M18 28h18M29 20l8 8-8 8" stroke="#12ac9e" stroke-width="4" fill="none"/></svg>
</a>

<div class="tab tab-1"><span class="num">01.</span><span class="lbl">Our<br>Information</span></div>
<div class="tab tab-2"><span class="num">02.</span><span class="lbl">Organization<br>Background</span></div>
<div class="tab tab-3"><span class="num">03.</span><span class="lbl">Ground<br>Transportation</span></div>

<p class="tab-text" style="top:872px">The Meridale Health Fund is pleased to announce the hosting of the annual Meridale Conference on Health Financing Initiatives, on November 12 - 14, 2013, at the Larkspur Bay Hotel in Montego Bay, Jamaica.<span class="more">READMORE..</span></p>
<p class="tab-text" style="top:990px">The inaugural conference was held in the Turks and Caicos in 2006, and since then other successful conferences have been held in Aruba in 2007, Trinidad and Tobago in 2008, Saint Marten in 2009, Bermuda in<span class="more">READMORE..</span></p>
<p class="tab-text" style="top:1106px">The Host country will provide shuttle service from the Airport to the Hotel and back, at no additional costs, for persons staying at the Larkspur Hotel. Persons staying outside of the Larkspur.<span class="more">READMORE..</span></p>

<div class="feature" style="top:869px;height:152px;background:linear-gradient(180deg,#8fb4d6,#a07a52)" role="img" aria-label="Photograph of the conference hotel terrace and grounds"><div class="caption">Official Conference Venue &amp; Hotel</div></div>
<div class="feature" style="top:1061px;height:157px;background:linear-gradient(135deg,#e8ecef,#cfd8de)" role="img" aria-label="Street map showing the route to the conference hotel"><div class="caption">Directions to Conference Hotel</div></div>

<h2 class="section-title">Featured Speakers</h2>

<div class="speaker" style="left:94px;top:1327px;background:var(--red)"><div class="photo" role="img" aria-label="Portrait of speaker" style="background:linear-gradient(#d8d4cc,#8a7a6a)"></div><div class="bio"><h3>Dr Lionel Ashcombe</h3><p>Dr Lionel Ashcombe was the recently retired Chief Medical Officer of the Ministry of Health, Trinidad and Tobago.</p></div></div>
<div class="speaker" style="left:438px;top:1327px;background:var(--orange)"><div class="photo" role="img" aria-label="Portrait of speaker" style="background:linear-gradient(#c9b9a4,#5a4234)"></div><div class="bio"><h3>Ms Renata Delsworth</h3><p>Ms. Renata Delsworth is a Research Fellow with the Verity Centre for Health Economics of Westmoor University</p></div></div>
<div class="speaker" style="left:782px;top:1327px;background:var(--blue)"><div class="photo" role="img" aria-label="Portrait of speaker" style="background:linear-gradient(#b8a48a,#5e4636)"></div><div class="bio"><h3>Dr Lionel Ashcombe</h3><p>Dr Lionel Ashcombe was the recently retired Chief Medical Officer of the Ministry of Health, Trinidad and Tobago.</p></div></div>
<div class="speaker" style="left:94px;top:1488px;background:var(--teal)"><div class="photo" role="img" aria-label="Portrait of speaker" style="background:linear-gradient(#dcd8d0,#6e5242)"></div><div class="bio"><h3>Dr Lionel Ashcombe</h3><p>Dr Lionel Ashcombe was the recently retired Chief Medical Officer of the Ministry of Health, Trinidad and Tobago.</p></div></div>
<div class="speaker" style="left:438px;top:1488px;background:var(--green)"><div class="photo" role="img" aria-label="Portrait of speaker" style="background:linear-gradient(#6fa0d0,#3a2a22)"></div><div class="bio"><h3>Ms Renata Delsworth</h3><p>Ms. Renata Delsworth is a Research Fellow with the Verity Centre for Health Economics of Westmoor University</p></div></div>
<div class="speaker" style="left:782px;top:1488px;background:var(--black)"><div class="photo" role="img" aria-label="Portrait of speaker" style="background:linear-gradient(#e2ddd6,#9a7e6a)"></div><div class="bio"><h3>Dr Lionel Ashcombe</h3><p>Dr Lionel Ashcombe was the recently retired Chief Medical Officer of the Ministry of Health, Trinidad and Tobago.</p></div></div>

<section class="sponsors">
  <span class="sponsor">Calder Wynn</span>
  <span class="sponsor">Tidemark</span>
  <span class="sponsor">Halvert Health</span>
  <span class="sponsor">bayline</span>
  <span class="sponsor">Kettering Reed's</span>
</section>

<footer class="site-footer">
  <div class="col" style="left:94px">
    <h4>Our Location</h4>
    <div role="img" aria-label="Map outline of Jamaica" style="width:170px;height:62px;background:var(--yellow);border-radius:40% 50% 45% 35%"></div>
    <p style="font-size:18px;margin-top:50px">Phone</p>
    <p style="font-size:18px">1-(555)-010-2200</p>
  </div>
  <div class="col" style="left:335px">
    <h4>Community Like Us</h4>
    <div style="display:flex;gap:10px;align-items:center;border-bottom:1px solid rgba(255,255,255,.5);padding-bottom:14px;width:214px">
      <span style="width:44px;height:44px;background:#000;display:block"></span>
      <span style="font-size:12px">MVAC<br>Like</span>
    </div>
    <div role="img" aria-label="Grid of member profile photos" style="width:214px;height:100px;margin-top:24px;background:linear-gradient(90deg,#6b5a4a,#c9a850,#2a5a8a)"></div>
  </div>
  <div class="col" style="left:608px">
    <h4>Quick Links</h4>
    <ul><li>Home</li><li>Conference</li><li>Programme</li><li>Speakers</li><li>Presentation</li><li>Hotel</li><li>Gallery</li><li>Contact us</li></ul>
  </div>
  <div class="col" style="left:858px">
    <h4>Quick Quote</h4>
    <div class="field">Name</div>
    <div class="field">Email</div>
    <div class="field tall">Comments</div>
    <div class="submit">Submit</div>
  </div>
</footer>
<div class="copyright">Copyright © 2015 MVAC2015</div>
<div class="strip" style="top:2229px"><span style="background:var(--blue)"></span><span style="background:var(--red)"></span><span style="background:var(--yellow)"></span><span style="background:var(--teal)"></span><span style="background:var(--green)"></span><span style="background:var(--orange)"></span></div>
</body>
</html>
```